Creative Landscape Architecture Company Needs a Creative Business Card Design

Varn and Partners, Inc. is a landscape architecture (LA) company started in 1997 in Austin, TX. We work on large commerical projects all around the U.S. and provide land planning, site planning, landscape design and architectural renderings.

We don't want this card to look like a LA firm's business card. We are looking for a business card design that is edgy and cool to reflect the more artistic and creative side of our company. We would like our clients to think "now there's a business card unlike any other LA that I've seen before."

We would like it to be in standard 2"x3.5" format. Double sided. Full color ok. Our company logo is attached. We like the logo but would not be adverse to any variations you would like to make to it. Feel free to change it up. Typically the logo has been a light saturated orange color but its not necessary that you stick with it.

Landscape

Requirements
Must have
• 1. Company name
2. individuals name
3. email address
4. cell number
5. office number
6. website: www.varnandpartners.example
7. Business address
Nice to have
• Can add (but not necessary)
Personal titles such as "president" or "registered landscape architect"

```html
<!DOCTYPE html>
<html lang="en">
<head>
<meta charset="utf-8">
<title>Varn and Partners, Inc. — Business Card</title>
<link rel="stylesheet" href="https://fonts.googleapis.com/css2?family=Source+Sans+3:wght@400;600;700&display=swap">
<style>
  :root {
    --ink: #000000;
    --paper: #ffffff;
    --stage: #e9e6e2;
    --card-shadow: rgba(0, 0, 0, 0.18);
  }
  html, body {
    margin: 0;
    padding: 0;
    width: 1200px;
    height: 402px;
    overflow: hidden;
    background: var(--stage);
  }
  .stage {
    position: relative;
    width: 1200px;
    height: 402px;
  }
  .card {
    position: absolute;
    top: 75px;
    width: 512px;
    height: 294px;
    box-shadow: 0 2px 8px var(--card-shadow);
  }
  .card--front { left: 60px; background: var(--paper); }
  .card--back  { left: 630px; background: var(--ink); }
  .card svg { display: block; width: 512px; height: 294px; }
  .card text { font-family: "Source Sans 3", "Myriad Pro", sans-serif; }
  .brand-mark { font-weight: 700; font-size: 21px; }
  .company-name { font-weight: 700; font-size: 19px; fill: var(--ink); }
  .person-name { font-weight: 700; font-size: 16px; fill: var(--ink); }
  .person-title { font-weight: 400; font-size: 12.5px; fill: var(--ink); }
  .contact { font-weight: 400; font-size: 12.5px; fill: var(--paper); }
  .back-url { font-weight: 400; font-size: 17px; letter-spacing: 1.2px; fill: var(--paper); }
</style>
</head>
<body>
<main class="stage">

  <section class="card card--front" aria-label="Card front">
    <svg viewBox="0 0 512 294" xmlns="http://www.w3.org/2000/svg">
      <!-- brand mark -->
      <g class="front-mark">
        <rect x="238" y="42" width="36" height="36" fill="var(--ink)"/>
        <text class="brand-mark" x="256" y="110" text-anchor="middle" fill="var(--ink)">Varn and Partners</text>
      </g>

      <text class="company-name" x="256" y="160" text-anchor="middle">Varn and Partners, Inc.</text>
      <text x="256" y="184" text-anchor="middle"><tspan class="person-name">Your name,</tspan><tspan class="person-title"> President</tspan></text>

      <!-- black footer band with swept top -->
      <path class="footer-band" d="M0 256 Q256 150 512 256 L512 294 L0 294 Z" fill="var(--ink)"/>
      <path class="footer-line" d="M0 248 Q256 142 512 248" fill="none" stroke="var(--ink)" stroke-width="1.6"/>

      <text class="contact" x="256" y="233" text-anchor="middle">Street Name, City Name, State Zip Code</text>

      <!-- office phone -->
      <g class="icon-phone" fill="var(--paper)">
        <path d="M57 252.5c-1.5 1.5-.8 4.5 1.6 6.9s5.4 3.1 6.9 1.6l.8-.8-2.2-2.2-1.1 1c-.8-.3-1.6-.9-2.3-1.6s-1.3-1.5-1.6-2.3l1-1.1-2.2-2.2z"/>
      </g>
      <text class="contact" x="68" y="262">555-014-2200</text>

      <!-- mobile -->
      <g class="icon-mobile">
        <rect x="174" y="251" width="6" height="11" rx="1" fill="var(--paper)"/>
        <rect x="175.3" y="252.5" width="3.4" height="5" fill="var(--ink)"/>
      </g>
      <text class="contact" x="184" y="262">555-014-2200</text>

      <!-- web -->
      <g class="icon-globe" fill="none" stroke="var(--paper)" stroke-width="1">
        <circle cx="298" cy="257" r="5"/>
        <ellipse cx="298" cy="257" rx="2.2" ry="5"/>
        <line x1="293" y1="257" x2="303" y2="257"/>
      </g>
      <text class="contact" x="307" y="262">www.varnandpartners.example</text>

      <text class="contact" x="256" y="281" text-anchor="middle">hello@varnandpartners.example</text>
    </svg>
  </section>

  <section class="card card--back" aria-label="Card back">
    <svg viewBox="0 0 512 294" xmlns="http://www.w3.org/2000/svg">
      <g class="back-mark">
        <rect x="236" y="88" width="40" height="40" fill="var(--paper)"/>
        <text class="brand-mark" x="256" y="162" text-anchor="middle" fill="var(--paper)">Varn and Partners</text>
      </g>
      <text class="back-url" x="256" y="251" text-anchor="middle">www.varnandpartners.example</text>
    </svg>
  </section>

</main>
</body>
</html>
```